8x8 Social Media Ad - Harbor Summit Expo

Attention Real Estate Agents
Please join us for our
Quarterly Real Estate Training Expo
The 2nd Saturday of February, May, August and November
Our Next Training Expo is _________________________________
From 9 am to 1 pm
at
Marlowe Suites Fernridge Station
4187 Copperleaf Lane, Greenbelt, MD 20770
Scheduled Speakers
9:00 am - Desmond Pryce - Orientation
9:30 am - Terrell Oakes - Multiple Income Streams / Keystone Track
10:00 am - Lorna Beckett - Marketing though Social Media
10:45 am - Raul Denning - Generating Business through Kelp-Nest
11:30 am - Tunde Adesemi - Real Estate Investing
12:15 pm - Marcus Oyelowo - (Main Speaker) Training Topic TBA
For more information call Desmond Pryce at (240) 555-0192 or email dpryce@harborsummithomes.example

```html
<!DOCTYPE html>
<html lang="en">
<head>
<meta charset="utf-8">
<title>Harbor Summit Expo – Quarterly Real Estate Training Expo</title>
<link rel="stylesheet" href="https://fonts.googleapis.com/css2?family=Poppins:wght@400;500;600;700;800&display=swap">
<style>
  :root{
    --teal:#1f939c;
    --teal-dark:#16717a;
    --ink:#0b0b0b;
    --paper:#ffffff;
    --grey-light:#eef0f0;
    --grey-mid:#a9acad;
  }
  *{box-sizing:border-box;margin:0;padding:0}
  html,body{width:1200px;height:1200px;overflow:hidden;background:var(--paper)}
  body{font-family:"Poppins",sans-serif;color:var(--ink)}
  .ad{position:relative;width:1200px;height:1200px;background:var(--paper);overflow:hidden}

  .hero-photo{position:absolute;left:660px;top:190px;width:540px;height:470px;
    background:radial-gradient(ellipse at 60% 45%,#8d9091 0%,#b9bbbc 35%,#e6e7e7 62%,rgba(255,255,255,0) 78%)}

  .brand{position:absolute;left:820px;top:70px;width:300px;display:flex;align-items:center;gap:12px}
  .brand-mark{width:28px;height:28px;background:var(--teal);flex:none}
  .brand-name{font-weight:700;font-size:27px;line-height:1.15;color:var(--teal)}

  .attention{position:absolute;left:57px;top:42px;font-weight:700;font-size:52px;line-height:1;color:var(--teal)}
  .audience{position:absolute;left:57px;top:88px;font-weight:500;font-size:50px;line-height:1.1}
  .invite{position:absolute;left:58px;top:152px;font-size:33px;font-weight:400}
  .quarterly{position:absolute;left:60px;top:205px;height:48px;width:258px}
  .quarterly svg{position:absolute;inset:0}
  .quarterly span{position:absolute;left:15px;top:3px;color:#fff;font-size:37px;font-weight:500;line-height:42px}
  .title{position:absolute;left:56px;top:252px;font-weight:800;font-size:90px;line-height:78px;letter-spacing:-2.5px;color:var(--teal)}
  .rule{position:absolute;left:60px;height:2px;width:640px;background:linear-gradient(90deg,var(--teal),rgba(31,147,156,.15))}
  .rule.top{top:437px}.rule.bottom{top:533px}
  .dates{position:absolute;left:61px;top:445px;font-size:37px;font-weight:500;line-height:40px}

  .next{position:absolute;left:59px;top:582px;font-size:28px;line-height:34px}
  .next b{font-weight:700}
  .divider{position:absolute;left:469px;top:580px;width:2px;height:74px;background:linear-gradient(180deg,transparent,var(--teal),transparent)}
  .venue{position:absolute;left:513px;top:586px;font-size:25px;line-height:31px}

  .band{position:absolute;left:0;top:792px;width:1200px;height:344px;background:var(--teal)}
  .main-photo{position:absolute;left:0;top:688px;width:400px;height:448px;
    background:radial-gradient(ellipse at 50% 40%,#6a4a38 0%,#3c2c24 45%,#22201f 75%,rgba(31,147,156,0) 100%)}
  .main-label{position:absolute;left:0;top:1073px;width:400px;height:61px}
  .main-label svg{position:absolute;inset:0}
  .main-label .name{position:absolute;left:0;width:395px;top:3px;text-align:center;color:var(--teal);font-weight:700;font-size:25px;line-height:30px}
  .main-label .role{position:absolute;left:0;width:395px;top:33px;text-align:center;color:#fff;font-size:15px;line-height:20px}

  .portrait{position:absolute;top:715px;width:145px;height:145px;border-radius:50%;box-shadow:0 4px 8px rgba(0,0,0,.25)}
  .p1{left:378px;background:radial-gradient(circle at 50% 40%,#b8b8b8,#5a5a5a 55%,#1c1c1c)}
  .p2{left:541px;background:radial-gradient(circle at 50% 40%,#8d6650,#474c5a 55%,#2a3558)}
  .p3{left:704px;background:radial-gradient(circle at 50% 45%,#c98a6a,#b5664e 55%,#0d0d0d)}
  .p4{left:865px;background:radial-gradient(circle at 50% 40%,#7b5644,#c9c9cb 55%,#f1f1f1)}
  .p5{left:1032px;background:radial-gradient(circle at 50% 40%,#4e3a30,#4f6d8a 55%,#5e7d4a)}

  .schedule{position:absolute;left:409px;top:895px;width:765px;height:243px;border:2px solid var(--ink);border-bottom:none;border-radius:28px 28px 0 0}
  .schedule-tab{position:absolute;left:617px;top:895px;width:352px;height:36px}
  .schedule-tab svg{position:absolute;inset:0}
  .schedule-tab span{position:absolute;inset:0;text-align:center;color:#fff;font-weight:700;font-size:22px;line-height:36px}
  .rows{position:absolute;left:427px;top:948px;width:747px;list-style:none}
  .row{height:29px;display:flex;align-items:center;color:#fff;font-size:20px;white-space:nowrap}
  .row:nth-child(odd){background:var(--teal-dark)}
  .time{width:100px;height:29px;line-height:29px;padding-left:5px}
  .row:nth-child(odd) .time{background:var(--ink)}
  .talk{padding-left:10px}
  .talk b{font-weight:700}

  .footer{position:absolute;left:0;width:1200px;top:1150px;text-align:center;font-size:20px;white-space:nowrap}
  .footer .hl{color:var(--teal);font-weight:700}
</style>
</head>
<body>
<main class="ad">
  <div class="hero-photo" role="img" aria-label="Black-and-white photo of real estate agents seated in a circle during a training session"></div>

  <div class="brand">
    <span class="brand-mark"></span>
    <span class="brand-name">Harbor Summit Realty Group</span>
  </div>

  <p class="attention">ATTENTION</p>
  <p class="audience">REAL ESTATE AGENTS</p>
  <p class="invite">Please Join Us for our</p>
  <div class="quarterly">
    <svg width="258" height="48" viewBox="0 0 258 48"><polygon points="0,0 232,0 246,48 0,48" fill="#0b0b0b"/><polygon points="232,0 244,0 258,48 246,48" fill="#1f939c"/></svg>
    <span>QUARTERLY</span>
  </div>
  <h1 class="title">REAL ESTATE<br>TRAINING EXPO</h1>
  <div class="rule top"></div>
  <p class="dates">The 2nd Saturday of February, May,<br>August and November</p>
  <div class="rule bottom"></div>

  <p class="next">Our <b>Next Training Expo</b> is<br>From 9 a.m. to 1 p.m.</p>
  <div class="divider"></div>
  <p class="venue">at Marlowe Suites Fernridge Station<br>4187 Copperleaf Lane, Greenbelt, MD 20770</p>

  <div class="band"></div>
  <div class="main-photo" role="img" aria-label="Portrait of main speaker Marcus Oyelowo"></div>
  <div class="main-label">
    <svg width="400" height="61" viewBox="0 0 400 61"><polygon points="0,0 375,0 400,61 0,61" fill="#0b0b0b"/></svg>
    <p class="name">Marcus Oyelowo</p>
    <p class="role">(Main Speaker) Training Topic TBA</p>
  </div>

  <div class="portrait p1" role="img" aria-label="Portrait of speaker Desmond Pryce"></div>
  <div class="portrait p2" role="img" aria-label="Portrait of speaker Terrell Oakes"></div>
  <div class="portrait p3" role="img" aria-label="Portrait of speaker Lorna Beckett"></div>
  <div class="portrait p4" role="img" aria-label="Portrait of speaker Raul Denning"></div>
  <div class="portrait p5" role="img" aria-label="Portrait of speaker Tunde Adesemi"></div>

  <section class="schedule" aria-label="Scheduled speakers"></section>
  <div class="schedule-tab">
    <svg width="352" height="36" viewBox="0 0 352 36"><path d="M0,0 H352 L336,28 Q331,36 320,36 H32 Q21,36 16,28 Z" fill="#0b0b0b"/></svg>
    <span>SCHEDULED SPEAKERS</span>
  </div>
  <ul class="rows">
    <li class="row"><span class="time">9:00 am</span><span class="talk">- <b>Desmond Pryce</b> - Orientation</span></li>
    <li class="row"><span class="time">9:30 am</span><span class="talk">- <b>Terrell Oakes</b> - Multiple Income Streams / Keystone Track</span></li>
    <li class="row"><span class="time">10:00 am</span><span class="talk">- <b>Lorna Beckett</b> - Marketing though Social Media</span></li>
    <li class="row"><span class="time">10:45 am</span><span class="talk">- <b>Raul Denning</b> - Generating Business through Kelp-Nest</span></li>
    <li class="row"><span class="time">11:30 am</span><span class="talk">- <b>Tunde Adesemi</b> - Real Estate Investing</span></li>
    <li class="row"><span class="time">12:15 pm</span><span class="talk">- <b>Marcus Oyelowo</b> - (Main Speaker) Training Topic TBA</span></li>
  </ul>

  <p class="footer">For more information <span class="hl">Call Desmond Pryce</span> at <span class="hl">(240) 555-0192</span> or email dpryce@harborsummithomes.example</p>
</main>
</body>
</html>
```